Wordpress Web Design For Midlifers.com

We're looking to update the design for www.midlifers.com. The website provides news and views for people aged 50 plus.

We want to use Wordpress as the content management tool and incorporate mailchimp to manage subscribers to our monthly newsletter.

In terms of design, we're looking for something simple and straightforward, we quite like the elder hub site, so something like that would be good. http://www.elderhub.org.uk
Updates

Project Deadline Extended
Reason: Dear All, Due to the Xmas break in the UK I've decided to extend the deadline by 7 days. Thanks for all your submissions, we will be making a decision shortly. Please note, as per the original brief, we are only interested in fully coded sites uploaded to our hosting provider. Please withdraw your design if you are not able to offer this complete solution. Thanks and good wishes to all!

Requirements
Must have
• Fully working wordpress templates that allow us to easily manage the website content. Easy for readers to use, navigate and read the content.
• Ideally a'turnkey' solution - the website built and ready for us to use wordpress to populate with content.

```html
<!DOCTYPE html>
<html lang="en">
<head>
<meta charset="utf-8">
<title>Midlifers.com – About Our Company</title>
<link rel="stylesheet" href="https://fonts.googleapis.com/css2?family=Open+Sans:wght@400;600;700&family=Arimo:wght@400&display=swap">
<style>
  :root{
    --ink:#3a3a3a;
    --body-text:#6b6b6b;
    --muted:#9a9a9a;
    --line:#dcdcdc;
    --brand-green:#8dc63f;
    --nav-teal:#5ad8d0;
    --nav-khaki:#b5b07e;
    --nav-salmon:#f4a09a;
    --nav-pink:#f06bb5;
    --nav-sage:#86b3a1;
    --nav-lavender:#d0a5ef;
    --nav-orange:#f9b070;
    --orange-top:#ffb25e;
    --orange-bottom:#ff8a1e;
    --purple-top:#bb6ee0;
    --purple-bottom:#8e3ecb;
    --donate-pink:#f07cbf;
    --footer-bg:#2b2b2b;
    --footer-text:#e6e6e6;
  }
  *{box-sizing:border-box;margin:0;padding:0}
  html,body{width:1200px;height:874px;overflow:hidden}
  body{
    position:relative;
    font-family:"Open Sans",Arial,sans-serif;
    color:var(--ink);
    background:linear-gradient(#ffffff 0,#ffffff 170px,#f6f6f6 260px,#ffffff 420px);
  }
  .brand{position:absolute;left:84px;top:44px;display:flex;align-items:center;gap:10px}
  .brand-dot{width:30px;height:30px;border-radius:50%;background:var(--brand-green)}
  .brand-name{font-size:26px;font-weight:700;color:var(--brand-green)}

  .search{position:absolute;left:825px;top:76px;width:295px;height:27px;border:1px solid #cfcfcf;border-radius:14px;background:#fff}
  .search span{position:absolute;left:15px;top:5px;font-size:11px;font-style:italic;color:#999}
  .search svg{position:absolute;right:9px;top:6px}

  .main-nav{position:absolute;left:79px;top:123px;width:1043px;height:50px;display:flex;border:1px solid var(--line);border-bottom:none;border-radius:3px 3px 0 0;background:linear-gradient(#ffffff,#f3f3f3)}
  .main-nav a{flex:1;text-decoration:none;color:#555;font-size:16px;text-align:center;line-height:46px;border-right:1px solid var(--line);border-bottom:4px solid}
  .main-nav a:last-child{border-right:none}

  .content-panel{position:absolute;left:80px;top:173px;width:1041px;height:565px;background:#fff;border-left:1px solid #e6e6e6;border-right:1px solid #e6e6e6}

  .article{position:absolute;left:109px;top:204px;width:680px}
  .article h1{font-size:26px;font-weight:400;color:#333;line-height:36px}
  .article .lead{font-size:14px;color:#444;line-height:22px;margin-top:3px}
  .article p{font-size:12.5px;color:var(--body-text);line-height:22px;margin-top:6px}
  .article p + p{margin-top:9px}

  .media-row{position:absolute;left:107px;top:452px;width:682px}
  .photo-frame{position:absolute;left:0;top:0;width:290px;height:163px;border:1px solid #ddd;background:#fff;box-shadow:0 1px 3px rgba(0,0,0,.12)}
  .photo-frame .photo{position:absolute;left:6px;top:6px;width:277px;height:150px;background:linear-gradient(180deg,#b9cde0 0%,#c9c2b4 40%,#6e8190 65%,#4a3f3c 100%)}
  .media-text{position:absolute;left:307px;top:0;width:375px}
  .media-text p{font-size:12.5px;color:var(--body-text);line-height:22px}
  .media-text p + p{margin-top:5px}
  .closing{position:absolute;left:107px;top:634px;width:682px;font-size:12.5px;color:var(--body-text);line-height:22px}

  .promo{position:absolute;left:815px;width:293px;border-radius:3px;color:#fff;padding:14px 22px}
  .promo h2{font-size:23px;font-weight:600;line-height:30px}
  .promo p{font-size:10.5px;line-height:15px;opacity:.9;margin-top:3px}
  .promo-register{top:184px;height:120px;background:linear-gradient(var(--orange-top),var(--orange-bottom));border:1px solid #f08a22}
  .promo-register .cta{display:block;margin-top:8px;font-size:12px;font-weight:700;color:#fff;text-decoration:none}
  .promo-newsletter{top:310px;height:135px;background:linear-gradient(var(--purple-top),var(--purple-bottom));border:1px solid #8a3fc4;padding-left:25px}
  .promo-newsletter h2{font-size:24px}
  .signup-field{margin-top:8px;width:245px;height:27px;background:#fff;border-radius:3px;position:relative}
  .signup-field svg{position:absolute;right:8px;top:4px}

  .donate-card{position:absolute;left:815px;top:451px;width:294px;height:216px;border:1px solid #e2e2e2;border-radius:3px;background:#fff}
  .donate-card .photo{height:128px;background:linear-gradient(135deg,#6a4a3c 0%,#9b6a4f 35%,#8fb6a0 60%,#c49b82 100%)}
  .donate-card h2{font-size:20px;font-weight:600;color:var(--donate-pink);margin:7px 0 0 20px}
  .donate-card p{font-size:10.5px;line-height:17px;color:var(--muted);margin:4px 20px 0}

  .site-footer{position:absolute;left:0;top:737px;width:1200px;height:137px;background:var(--footer-bg);font-family:"Arimo",Arial,sans-serif;color:var(--footer-text)}
  .footer-nav{position:absolute;left:104px;font-size:14.5px;display:flex}
  .footer-nav a{color:var(--footer-text);text-decoration:none}
  .footer-nav .sep{margin:0 26px}
  .footer-nav.primary{top:27px}
  .footer-nav.secondary{top:56px;left:102px}
  .footer-nav.secondary .sep{margin:0 25px}
  .copyright{position:absolute;left:102px;top:88px;font-size:10.5px}
  .social-box{position:absolute;left:1074px;top:22px;width:20px;height:32px;background:#fff;border-radius:2px}
</style>
</head>
<body>
  <header>
    <div class="brand">
      <span class="brand-dot"></span>
      <span class="brand-name">Midlifers.com</span>
    </div>
    <div class="search">
      <span>Search here..</span>
      <svg width="15" height="15" viewBox="0 0 15 15"><circle cx="6" cy="6" r="4.8" fill="none" stroke="#777" stroke-width="1.6"/><line x1="9.5" y1="9.5" x2="13.5" y2="13.5" stroke="#777" stroke-width="1.8" stroke-linecap="round"/></svg>
    </div>
    <nav class="main-nav">
      <a href="#" style="border-bottom-color:var(--brand-green)">Home</a>
      <a href="#" style="border-bottom-color:var(--nav-teal)">Travel</a>
      <a href="#" style="border-bottom-color:var(--nav-khaki)">Health</a>
      <a href="#" style="border-bottom-color:var(--nav-salmon)">Hobbies</a>
      <a href="#" style="border-bottom-color:var(--nav-pink)">Lifestyle</a>
      <a href="#" style="border-bottom-color:var(--nav-sage)">Insurance</a>
      <a href="#" style="border-bottom-color:var(--nav-lavender)">Legal</a>
      <a href="#" style="border-bottom-color:var(--nav-orange)">Competitions</a>
      <a href="#" style="border-bottom-color:var(--brand-green)">Survey</a>
    </nav>
  </header>

  <div class="content-panel"></div>

  <main>
    <article class="article">
      <h1>About Our Company</h1>
      <p class="lead">Lorem ipsum dolor sit amet, consectetuer adipiscing elit. Nam cursus. Morbi ut mi. Nullam enim leo, egestas id, condimentum at, laoreet mattis, massa.</p>
      <p>Phasellus felis dolor, scelerisque a, tempus eget, lobortis id, libero. Aliquam nec erat at purus cursus interdum. Vestibulum ligula augue, bibendum accumsan, vestibulum ut, commodo a, mi. Morbi ornare gravida elit. Integer congue, augue et malesuada iaculis, ipsum dui aliquet felis, at cursus magna nisl nec elit. Vestibulum gravida. Praesent elementum elit at tellus. Malesuada nec, ultricies sit amet, porttitor mattis, enim.</p>
      <p>In massa libero, interdum nec, interdum vel, blandit sed, nulla. In ullamcorper, est eget tempor cursus, neque mi consectetuer mi, a ultricies massa est sed nisl.</p>
    </article>

    <section class="media-row">
      <figure class="photo-frame">
        <div class="photo" role="img" aria-label="Photo of an older couple on a gondola ride along a Venice canal"></div>
      </figure>
      <div class="media-text">
        <p>Pellentesque faucibus. Ut accumsan ultricies elit. Maecenas at justo id velit placerat molestie. Donec dictum lectus non odio. Cras a ante vitae enim iaculis aliquam.</p>
        <p>Mauris nunc quam, venenatis nec, euismod sit amet, egestas placerat, est. Pellentesque habitant morbi tristique senectus et netus et malesuada fames ac turpis egestas. Cras id elit. Integer quis urna. Ut ante enim, dapibus malesuada fringilla</p>
      </div>
    </section>
    <p class="closing">Etiam est nunc, venenatis in, tristique eu, imperdiet ac, nisl. Cum sociis natoque penatibus et magnis dis parturient montes, nascetur ridiculus mus. In iaculis facilisis massa. Etiam eu urna. Sed porta. Suspendisse quam leo, molestie sed, luctus quis, feugiat in, pede. Fusce tellus. Sed metus augue, convallis et</p>
  </main>

  <aside>
    <section class="promo promo-register">
      <h2>Register Now</h2>
      <p>Cum sociis natoque penatibus et magnis dis parturient montes, nascetur ridiculus mus</p>
      <a class="cta" href="#">CLICK HERE TO REGISTER NOW ›</a>
    </section>
    <section class="promo promo-newsletter">
      <h2>Sign Up Newsletters</h2>
      <p>Cum sociis natoque penatibus et magnis dis parturient montes, nascetur ridiculus mus</p>
      <div class="signup-field">
        <svg width="20" height="20" viewBox="0 0 20 20"><circle cx="10" cy="10" r="8.5" fill="none" stroke="#999" stroke-width="1.6"/><path d="M5.5 10h8M10 6.5l3.5 3.5-3.5 3.5" fill="none" stroke="#999" stroke-width="1.8"/></svg>
      </div>
    </section>
    <section class="donate-card">
      <div class="photo" role="img" aria-label="Photo of volunteers sorting donated clothing outside a charity shop"></div>
      <h2>Donate today</h2>
      <p>Cum sociis natoque penatibus et magnis dis parturient montes, nascetur ridiculus mus</p>
    </section>
  </aside>

  <footer class="site-footer">
    <nav class="footer-nav primary">
      <a href="#">Home</a><span class="sep">|</span>
      <a href="#">Travel</a><span class="sep">|</span>
      <a href="#">Health</a><span class="sep">|</span>
      <a href="#">Hobbies</a><span class="sep">|</span>
      <a href="#">Lifestyle</a><span class="sep">|</span>
      <a href="#">Insurance</a><span class="sep">|</span>
      <a href="#">Legal</a><span class="sep">|</span>
      <a href="#">Competitions</a><span class="sep">|</span>
      <a href="#">Survey</a>
    </nav>
    <nav class="footer-nav secondary">
      <a href="#">About Us</a><span class="sep">|</span>
      <a href="#">Advertise</a><span class="sep">|</span>
      <a href="#">Support</a><span class="sep">|</span>
      <a href="#">Blog</a><span class="sep">|</span>
      <a href="#">Contact</a>
    </nav>
    <p class="copyright">Copyright © 2013 Midlifers. All Rights Reserved.</p>
    <span class="social-box" role="img" aria-label="Social network link"></span>
  </footer>
</body>
</html>
```